New Look Driving School Project

Current website:
www. kelmorawheelacademy.com

Websites that we like (use content and courses from here as well):
https://www. tollbenroadclass.com

We are looking for a fresh looking driving school website that is easy for students to find the course they are looking for, the price, and allow them to book a lesson all on our website. We would like for this website to have multiple pages: Home, Teen Courses, Adult Courses, About Us, Contact, FAQ, Blog, Requirements.

Target Market(s)

Students in High School or Parents

Industry/Entity Type

Education

Coding

Coded - Design and coding required

Number of Pages Required

5+ page

Font styles to use
Serif
Sans Serif

Colors

Designer to choose colors to be used in the design.

Requirements
Must have
• Must have a form submission and payment processing option. Must have the ability to pick a course, see available times, and process their payment online. MUST BE MOBILE FRIENDLY DESIGN.
Nice to have
• Nice to have a clean format, with big bold fonts.
Should not have
• Should not have a lot of sliders or animations. Should be very fast loading on mobile. Keep it simple but easy to read and elegant.

```html
<!DOCTYPE html>
<html lang="en">
<head>
<meta charset="utf-8">
<title>Kelmora Wheel Academy</title>
<link href="https://fonts.googleapis.com/css2?family=Montserrat:wght@400;500;600;700;800&family=Open+Sans:wght@400;600;700&display=swap" rel="stylesheet">
<style>
:root{
  --navy:#101c3a;
  --navy-2:#0b1530;
  --red:#ec1b4b;
  --white:#ffffff;
  --ink:#1d2433;
  --muted:#6b7180;
  --line:#e3e5ea;
  --light:#f4f5f7;
  --blue:#1e8fe0;
  --green:#35b54a;
  --green-2:#47b94a;
  --orange:#f26a21;
}
*{box-sizing:border-box;margin:0;padding:0}
html,body{width:1200px;height:4417px;overflow:hidden}
body{font-family:"Open Sans",Arial,sans-serif;color:var(--ink);background:var(--white);position:relative}
h1,h2,h3,h4,.heading{font-family:"Montserrat",Arial,sans-serif}
.abs{position:absolute}
.btn{display:inline-block;background:var(--red);color:var(--white);font-family:"Montserrat",sans-serif;font-weight:700;font-size:13px;letter-spacing:.5px;text-transform:uppercase;padding:12px 26px;border-radius:2px}
.red{color:var(--red)}

/* top bar */
.topbar{left:0;top:0;width:1200px;height:124px;background:var(--white)}
.brand{left:188px;top:40px;display:flex;align-items:center;gap:12px}
.brand-dot{width:40px;height:40px;border-radius:50%;background:var(--red)}
.brand-name{font-family:"Montserrat",sans-serif;font-weight:700;font-size:19px;color:var(--navy)}
.top-info{top:30px;font-size:13px;color:var(--ink);display:flex;align-items:center;gap:8px}
.top-info svg{width:16px;height:16px}
.call-btn{left:980px;top:62px;padding:10px 28px}

/* nav */
.nav{left:0;top:124px;width:1200px;height:30px;background:var(--navy)}
.nav ul{list-style:none;display:flex;gap:34px;position:absolute;left:188px;top:8px}
.nav li{color:var(--white);font-family:"Montserrat",sans-serif;font-size:12px;font-weight:600;text-transform:uppercase}

/* hero */
.hero{left:0;top:154px;width:1200px;height:474px;background:linear-gradient(100deg,#2c3548 0%,#5e6a7b 35%,#9aa1a9 60%,#3e4656 100%)}
.hero-title{left:188px;top:200px;color:var(--white)}
.hero-title span{display:block;font-size:40px;font-weight:600}
.hero-title strong{display:block;font-size:46px;font-weight:800}
.hero-strip{left:0;top:406px;width:1200px;height:68px;background:rgba(11,21,48,.85)}
.hero-feat{top:410px;height:60px;width:205px;display:flex;align-items:center;gap:10px;padding-left:16px;color:var(--white);font-size:11px}
.hero-feat b{display:block;font-family:"Montserrat",sans-serif;font-size:13px}
.hero-feat.active{background:var(--red)}
.hero-feat svg{width:26px;height:26px;flex:none}

.details-form{left:828px;top:154px;width:284px;height:474px;background:var(--white);padding:26px 22px}
.details-form h3{font-size:18px;font-weight:800;text-transform:uppercase;color:var(--navy)}
.details-form p{font-size:10px;color:var(--muted);margin:4px 0 16px}
.field{height:40px;border:1px solid var(--line);margin-bottom:14px;font-size:12px;color:var(--muted);padding:11px 14px}
.field-row{display:flex;gap:10px}
.field-row .field{flex:1}
.details-form .btn{width:100%;text-align:center;margin-top:10px}

/* features */
.features{left:0;top:628px;width:1200px;height:672px;background:var(--light)}
.section-title{width:1200px;text-align:center;font-size:26px;font-weight:600;color:var(--navy);text-transform:uppercase;line-height:1.25}
.section-title b{font-weight:800}
.feature{top:784px;width:202px;height:356px;background:var(--white)}
.feature-top{height:164px;display:flex;align-items:center;justify-content:center}
.feature-top svg{width:64px;height:64px}
.feature h4{text-align:center;font-size:16px;font-weight:700;margin:22px 0 14px}
.feature p{font-size:11.5px;line-height:1.6;color:var(--muted);text-align:center;padding:0 16px}

/* courses */
.courses{left:0;top:1300px;width:1200px;height:688px;background:linear-gradient(135deg,#1a2540,#26314d 50%,#141e38)}
.courses .section-title{color:var(--white)}
.tabs{width:1200px;top:1436px;text-align:center;color:var(--white);font-size:13px}
.tabs span{padding:0 10px}
.tabs .on{border-bottom:2px solid var(--red);padding-bottom:4px}
.course{width:276px;height:82px;background:var(--white);display:flex;align-items:center;gap:14px;padding:0 18px}
.course-icon{width:42px;height:42px;border-radius:50%;border:3px solid var(--red);flex:none;display:flex;align-items:center;justify-content:center}
.course-icon svg{width:22px;height:22px}
.course span{font-family:"Montserrat",sans-serif;font-size:12px;font-weight:700;text-transform:uppercase;color:var(--ink);line-height:1.4}

/* about */
.about{left:0;top:1988px;width:1200px;height:492px;background:linear-gradient(90deg,#c8661d 0%,#e7a045 30%,#6d6f77 55%,#3c4453 100%)}
.about-card{left:188px;top:2020px;width:344px;height:440px;background:var(--white);padding:26px 22px}
.about-card h2{font-size:24px;font-weight:800;text-transform:uppercase}
.about-card p{font-size:11.5px;line-height:1.6;color:var(--muted);margin:10px 0 16px}
.about-card h4{font-size:15px;margin-bottom:10px}
.about-card ul{list-style:none;font-size:12.5px;line-height:2}
.about-card li::before{content:"•";color:var(--red);margin-right:8px}
.about-card .btn{margin-top:18px}
.offer{left:648px;top:2196px;width:392px;height:244px;background:var(--navy);padding:26px}
.offer h3{color:var(--white);font-size:28px;font-weight:800;text-transform:uppercase;line-height:1.15}
.offer p{color:#c5cad6;font-size:11px;line-height:1.6;margin:14px 0;width:260px;margin-left:auto}
.offer .btn{margin-left:132px}

/* stats */
.stats{left:0;top:2480px;width:1200px;height:164px;background:var(--navy-2);display:flex;justify-content:center}
.stat{width:300px;text-align:center;padding-top:44px;color:var(--white);border-right:1px solid rgba(255,255,255,.2)}
.stat:last-child{border-right:none}
.stat b{display:block;font-family:"Montserrat",sans-serif;font-size:38px;font-weight:800}
.stat span{font-size:12px;text-transform:uppercase;letter-spacing:.5px}

/* gallery */
.gallery-head{left:188px;top:2726px}
.gallery-head h2{font-size:24px;font-weight:800;text-transform:uppercase}
.gallery-head p{font-size:11.5px;color:var(--muted);line-height:1.6;width:520px;margin-top:8px}
.gallery-tabs{left:188px;top:2862px;display:flex;gap:28px;align-items:center;font-size:12px}
.gallery-tabs .on{background:var(--red);color:var(--white);padding:5px 16px;border-radius:12px}
.photo{width:214px;height:216px}

/* video */
.video{left:0;top:3456px;width:1200px;height:368px;background:linear-gradient(120deg,#111a33,#2c3650 45%,#1a2440)}
.play{left:570px;top:3580px;width:60px;height:60px;border-radius:50%;background:var(--red)}
.video-title{width:1200px;top:3660px;text-align:center;color:var(--white);font-size:22px;font-weight:800;text-transform:uppercase}

/* faq */
.faq{left:0;top:3824px;width:1200px;height:292px;background:linear-gradient(180deg,#eef0f2,#dfe3e7)}
.faq .section-title{color:var(--navy)}
.faq-list{left:300px;top:3920px;width:600px;list-style:none}
.faq-list li{font-size:12px;font-weight:700;margin-bottom:14px;padding-left:18px;position:relative}
.faq-list li::before{content:"";position:absolute;left:0;top:4px;width:8px;height:8px;background:var(--red);border-radius:50%}
.faq-list li p{font-weight:400;color:var(--muted);font-size:11px;line-height:1.6;margin-top:6px}

/* footer */
.footer{left:0;top:4116px;width:1200px;height:301px;background:var(--navy)}
.f-col{top:4140px;color:var(--white);width:210px}
.f-col h4{font-size:14px;font-weight:700;margin-bottom:14px}
.f-col p{font-size:11px;line-height:1.6;color:#c1c6d2}
.f-line{font-size:11px;color:#c1c6d2;margin-top:8px;display:flex;align-items:center;gap:8px}
.socials{display:flex;gap:8px;margin-top:12px}
.socials i{width:14px;height:14px;border-radius:50%;background:#c1c6d2;display:block}
.f-field{height:30px;background:var(--white);margin-bottom:8px;font-size:10px;color:var(--muted);padding:8px 10px}
.f-field.tall{height:56px}
.f-btn{padding:8px 18px;font-size:11px}
.map{width:180px;height:140px;background:linear-gradient(135deg,#e6e8e2,#cfd7cf)}
.copyright{left:0;top:4388px;width:1200px;height:29px;background:var(--navy-2);color:#9aa0ae;font-size:11px;text-align:center;padding-top:8px}
</style>
</head>
<body>

<header class="topbar abs">
  <div class="brand abs"><span class="brand-dot"></span><span class="brand-name">Kelmora Wheel Academy</span></div>
  <div class="top-info abs" style="left:600px">
    <svg viewBox="0 0 16 16"><circle cx="8" cy="8" r="6.5" fill="none" stroke="#ec1b4b" stroke-width="1.5"/><path d="M8 4v4l3 2" fill="none" stroke="#ec1b4b" stroke-width="1.5"/></svg>
    Mon - Sat 8:00 AM - 7:00 PM
  </div>
  <div class="top-info abs" style="left:880px">
    <svg viewBox="0 0 16 16"><path d="M4 2l2 3-1.5 1.5c.8 1.8 2.2 3.2 4 4L10 9l3 2-1.5 2.5C7 13 3 9 2.5 4.5z" fill="#ec1b4b"/></svg>
    (555) 014-2298
  </div>
  <div class="top-info abs" style="left:1000px">
    <svg viewBox="0 0 16 16"><circle cx="8" cy="5" r="3" fill="#ec1b4b"/><path d="M2 15c0-4 12-4 12 0z" fill="#ec1b4b"/></svg>
    Sign up / login
  </div>
  <span class="btn call-btn abs">Call Us</span>
</header>

<nav class="nav abs">
  <ul><li>Home</li><li>Teen Courses</li><li>Adult Courses</li><li>About Us</li><li>Contact</li><li>FAQ</li><li>Blog</li><li>Requirements</li></ul>
</nav>

<section class="hero abs" role="img" aria-label="Photo of a young driver at the wheel with an instructor beside her"></section>
<div class="hero-title abs"><span>Welcome to</span><strong>Kelmora Wheel Academy</strong></div>
<div class="hero-strip abs"></div>
<div class="hero-feat active abs" style="left:188px">
  <svg viewBox="0 0 26 26"><rect x="3" y="5" width="20" height="13" rx="1" fill="none" stroke="#fff" stroke-width="2"/><path d="M9 22h8" stroke="#fff" stroke-width="2"/></svg>
  <div><b>ONLINE</b>Driver classes</div>
</div>
<div class="hero-feat abs" style="left:393px">
  <svg viewBox="0 0 26 26"><circle cx="13" cy="13" r="10" fill="none" stroke="#fff" stroke-width="2"/><circle cx="13" cy="13" r="3" fill="#fff"/></svg>
  <div><b>LESSONS</b>Behind the wheel</div>
</div>
<div class="hero-feat abs" style="left:598px">
  <svg viewBox="0 0 26 26"><rect x="4" y="8" width="18" height="10" rx="2" fill="none" stroke="#fff" stroke-width="2"/><circle cx="8" cy="20" r="2" fill="#fff"/><circle cx="18" cy="20" r="2" fill="#fff"/></svg>
  <div><b>LICENSE</b>Road test prep</div>
</div>

<form class="details-form abs">
  <h3>Send us <span class="red">your details</span></h3>
  <p>We will call you back within one business day.</p>
  <div class="field">Enter your name</div>
  <div class="field">Enter your email</div>
  <div class="field">Enter your phone</div>
  <div class="field">Select a course</div>
  <div class="field-row"><div class="field">Date</div><div class="field">Time</div></div>
  <div class="field-row"><div class="field">Pick-up</div><div class="field">Drop-off</div></div>
  <span class="btn">Pick Courses</span>
</form>

<section class="features abs"></section>
<h2 class="section-title abs" style="top:676px">The most advanced driving school<br><b>in Virginia</b></h2>

<div class="feature abs" style="left:188px">
  <div class="feature-top" style="background:var(--blue)"><svg viewBox="0 0 64 64"><path d="M10 40l14-4 10 4 18-10v6L34 46l-10-4-14 4z" fill="#fff"/><circle cx="36" cy="20" r="8" fill="none" stroke="#fff" stroke-width="3"/></svg></div>
  <h4>Affordable</h4>
  <p>Quality lessons at fair prices, with flexible packages and payment plans that suit every family budget.</p>
</div>
<div class="feature abs" style="left:418px">
  <div class="feature-top" style="background:var(--green)"><svg viewBox="0 0 64 64"><path d="M14 30h8v22h-8zM26 30l8-16c4 0 5 3 4 7l-2 7h12c3 0 4 3 3 5l-5 15c-1 2-2 4-5 4H26z" fill="#fff"/></svg></div>
  <h4>Experience</h4>
  <p>Our certified instructors bring years of road teaching and thousands of happy students behind the wheel.</p>
</div>
<div class="feature abs" style="left:648px">
  <div class="feature-top" style="background:var(--green-2)"><svg viewBox="0 0 64 64"><path d="M32 8l20 8v14c0 13-9 22-20 26C21 52 12 43 12 30V16z" fill="none" stroke="#fff" stroke-width="3"/><path d="M23 32l7 7 12-13" fill="none" stroke="#fff" stroke-width="3"/></svg></div>
  <h4>Guarantee</h4>
  <p>We stand behind every lesson and guarantee your satisfaction with the training our instructors provide.</p>
</div>
<div class="feature abs" style="left:878px">
  <div class="feature-top" style="background:var(--orange)"><svg viewBox="0 0 64 64"><rect x="14" y="8" width="36" height="46" rx="2" fill="none" stroke="#fff" stroke-width="3"/><path d="M22 22h20M22 30h20M22 38h12" stroke="#fff" stroke-width="3"/></svg></div>
  <h4>Certified</h4>
  <p>All of our instructors are fully certified by the State Motor Vehicle Office and trained to teach safely.</p>
</div>
<span class="btn abs" style="left:554px;top:1180px">Read More</span>

<section class="courses abs" role="img" aria-label="Dim photo of a smiling student and instructor in a car"></section>
<h2 class="section-title abs" style="top:1376px">Our <b>Courses</b></h2>
<div class="tabs abs"><span class="on">Teen Courses</span>|<span>Adult Courses</span></div>

<div class="course abs" style="left:188px;top:1496px"><div class="course-icon"><svg viewBox="0 0 22 22"><rect x="3" y="9" width="16" height="7" rx="2" fill="#ec1b4b"/><path d="M6 9l2-4h6l2 4" fill="none" stroke="#ec1b4b" stroke-width="2"/></svg></div><span>Behind the wheel $255</span></div>
<div class="course abs" style="left:508px;top:1496px"><div class="course-icon"><svg viewBox="0 0 22 22"><rect x="3" y="9" width="16" height="7" rx="2" fill="#ec1b4b"/><path d="M6 9l2-4h6l2 4" fill="none" stroke="#ec1b4b" stroke-width="2"/></svg></div><span>Private 1 on 1 driving $400</span></div>
<div class="course abs" style="left:828px;top:1496px"><div class="course-icon"><svg viewBox="0 0 22 22"><rect x="3" y="9" width="16" height="7" rx="2" fill="#ec1b4b"/><path d="M6 9l2-4h6l2 4" fill="none" stroke="#ec1b4b" stroke-width="2"/></svg></div><span>45 days waiver package $405</span></div>
<div class="course abs" style="left:188px;top:1640px"><div class="course-icon"><svg viewBox="0 0 22 22"><rect x="3" y="9" width="16" height="7" rx="2" fill="#ec1b4b"/><path d="M6 9l2-4h6l2 4" fill="none" stroke="#ec1b4b" stroke-width="2"/></svg></div><span>Platinum $599</span></div>
<div class="course abs" style="left:508px;top:1640px"><div class="course-icon"><svg viewBox="0 0 22 22"><rect x="3" y="9" width="16" height="7" rx="2" fill="#ec1b4b"/><path d="M6 9l2-4h6l2 4" fill="none" stroke="#ec1b4b" stroke-width="2"/></svg></div><span>8 hour lesson plus 1 road test $239</span></div>
<div class="course abs" style="left:828px;top:1640px"><div class="course-icon"><svg viewBox="0 0 22 22"><rect x="3" y="9" width="16" height="7" rx="2" fill="#ec1b4b"/><path d="M6 9l2-4h6l2 4" fill="none" stroke="#ec1b4b" stroke-width="2"/></svg></div><span>Driving refresher package $250</span></div>
<div class="course abs" style="left:188px;top:1784px"><div class="course-icon"><svg viewBox="0 0 22 22"><rect x="3" y="9" width="16" height="7" rx="2" fill="#ec1b4b"/><path d="M6 9l2-4h6l2 4" fill="none" stroke="#ec1b4b" stroke-width="2"/></svg></div><span>Silver package $399</span></div>
<div class="course abs" style="left:508px;top:1784px"><div class="course-icon"><svg viewBox="0 0 22 22"><rect x="3" y="9" width="16" height="7" rx="2" fill="#ec1b4b"/><path d="M6 9l2-4h6l2 4" fill="none" stroke="#ec1b4b" stroke-width="2"/></svg></div><span>Gold package $549</span></div>
<div class="course abs" style="left:828px;top:1784px"><div class="course-icon"><svg viewBox="0 0 22 22"><rect x="3" y="9" width="16" height="7" rx="2" fill="#ec1b4b"/><path d="M6 9l2-4h6l2 4" fill="none" stroke="#ec1b4b" stroke-width="2"/></svg></div><span>Diamond package $849</span></div>

<section class="about abs" role="img" aria-label="Photo of a busy highway at sunset"></section>
<div class="about-card abs">
  <h2>About <span class="red">Us</span></h2>
  <p>We are experts in teen driving education, helping new drivers and parents with friendly, patient, certified instructors.</p>
  <h4>We Specialize in</h4>
  <ul>
    <li>Behind the Wheel for Teens and Adults</li>
    <li>Learners Permits</li>
    <li>Drivers Education</li>
    <li>Classroom Courses and Various Courses</li>
    <li>Driver Improvement Course</li>
  </ul>
  <span class="btn">Send Request</span>
</div>
<div class="offer abs">
  <h3>Save 10% <span class="red">order</span><br><span class="red">now</span></h3>
  <p>Book your complete course online today and save on every lesson package.</p>
  <span class="btn">Order Now</span>
</div>

<section class="stats abs">
  <div class="stat"><b>100%</b><span>Satisfaction guaranteed</span></div>
  <div class="stat"><b>20,000</b><span>Hours of teaching</span></div>
  <div class="stat"><b>FREE</b><span>Pick up and drop off</span></div>
</section>

<div class="gallery-head abs">
  <h2>Photo <span class="red">Gallery</span></h2>
  <p>A look at our students and instructors on the road, in the classroom and on test day with our fleet of training cars.</p>
</div>
<div class="gallery-tabs abs"><span class="on">All</span><span>Cars</span><span>Classroom</span></div>
<div class="photo abs" style="left:188px;top:2932px;background:linear-gradient(135deg,#6e8fb5,#c4b7a5)" role="img" aria-label="Photo of a student driver with instructor"></div>
<div class="photo abs" style="left:422px;top:2932px;background:linear-gradient(135deg,#9bb0c6,#c98a4a)" role="img" aria-label="Photo of a parking lot training course with cones"></div>
<div class="photo abs" style="left:656px;top:2932px;background:linear-gradient(135deg,#c8ccd2,#5d6878)" role="img" aria-label="Photo of a training car on a test course"></div>
<div class="photo abs" style="left:890px;top:2932px;background:linear-gradient(135deg,#8fa7c4,#d9cbb6)" role="img" aria-label="Photo of an instructor guiding a driver"></div>
<div class="photo abs" style="left:188px;top:3172px;background:linear-gradient(135deg,#7b8a74,#b9b2a2)" role="img" aria-label="Photo of a student walking to a car"></div>
<div class="photo abs" style="left:422px;top:3172px;background:linear-gradient(135deg,#3a3f4a,#8b8f98)" role="img" aria-label="Photo of a car dashboard and steering wheel"></div>
<div class="photo abs" style="left:656px;top:3172px;background:linear-gradient(135deg,#2b2f3a,#c9c3b7)" role="img" aria-label="Photo of a handshake after a passed road test"></div>
<div class="photo abs" style="left:890px;top:3172px;background:linear-gradient(135deg,#b7bcc2,#e07a2f)" role="img" aria-label="Photo of cones on a parking practice road"></div>

<section class="video abs" role="img" aria-label="Dim photo of a student driving with an instructor"></section>
<div class="play abs"><svg viewBox="0 0 60 60" width="60" height="60"><path d="M24 18l18 12-18 12z" fill="#fff"/></svg></div>
<h2 class="video-title abs">See <span class="red">Video Presentation</span></h2>

<section class="faq abs" role="img" aria-label="Faded photo of an open road with road signs"></section>
<h2 class="section-title abs" style="top:3868px"><b>FAQ</b></h2>
<ul class="faq-list abs">
  <li>How old must I be to start a driving course?
    <p>Students can begin classroom lessons at fifteen and behind the wheel training once a learners permit is issued.</p>
  </li>
  <li>How do I book a lesson and pay online?</li>
  <li>Do you offer free pick up and drop off?</li>
  <li>What should I bring to my first lesson?</li>
  <li>Can parents join the road test practice?</li>
</ul>

<footer class="footer abs"></footer>
<div class="f-col abs" style="left:188px">
  <h4>Contact</h4>
  <p>Reach our team with any question about courses, schedules or payments and we will reply fast.</p>
  <div class="f-line"><svg width="12" height="12" viewBox="0 0 16 16"><circle cx="8" cy="8" r="6.5" fill="none" stroke="#ec1b4b" stroke-width="1.5"/><path d="M8 4v4l3 2" fill="none" stroke="#ec1b4b" stroke-width="1.5"/></svg>Mon - Fri 8:00 - 7:00</div>
  <div class="f-line"><svg width="12" height="12" viewBox="0 0 16 16"><path d="M4 2l2 3-1.5 1.5c.8 1.8 2.2 3.2 4 4L10 9l3 2-1.5 2.5C7 13 3 9 2.5 4.5z" fill="#ec1b4b"/></svg>(555) 014-2298</div>
  <div class="socials"><i></i><i></i><i></i><i></i></div>
</div>
<div class="f-col abs" style="left:428px">
  <h4>Quick Contact</h4>
  <div class="f-field">Name</div>
  <div class="f-field">Email</div>
  <div class="f-field tall">Message</div>
  <span class="btn f-btn">Submit</span>
</div>
<div class="f-col abs" style="left:668px">
  <h4>Newsletter</h4>
  <p>Subscribe to our newsletter for latest updates.</p>
  <div class="f-field" style="margin-top:10px">E-mail</div>
  <span class="btn f-btn">Subscribe</span>
</div>
<div class="f-col abs" style="left:908px">
  <h4>Locate Us</h4>
  <div class="map" role="img" aria-label="Street map showing the school location"></div>
</div>
<div class="copyright abs">© copyright Kelmora Wheel Academy 2019. All rights reserved.</div>

</body>
</html>
```